Baby Boutique Needs a Business Card Design

We need a modern double sided business card design using the attached logo for Lil' Tot Nook.

Lil' Tot Nook is a baby boutique which sells only handmade clothing and accessories for both boys and girls. Our store will live exclusively online.

We would like to only use the colors that have been used in the logo.

Target Market(s)

Potential wholesale clients, Small business owners

Industry/Entity Type

Retail

Contact Information for Business Card

Name Wendell J. Ferris (Owner)
Email sales@ltotnook.com
Main Phone 787-203-6159
Cell phone 787-203-6742
Website www.LTotNook.com

Font styles to use
Sans Serif

Colors

Designer to choose colors to be used in the design.

Requirements
Must have
• -Would like to have icons that indentify the contact information.
• -Include our website
• -Include our tagline in a small area near the bottom. "Handmade Baby Creations"
• -Would like to include Facebook and Instagram Icons
• -
Nice to have
• Would like to have a simple back side with the logo.
• Something along the lines of the harbor ledger card attached.

```html
<!DOCTYPE html>
<html lang="en">
<head>
<meta charset="utf-8">
<title>Lil' Tot Nook — Business Cards</title>
<link rel="stylesheet" href="https://fonts.googleapis.com/css2?family=Questrial&family=Open+Sans:wght@300;400&display=swap">
<style>
  :root {
    --navy: #1f2532;
    --teal: #76cbbd;
    --paper: #ffffff;
  }
  * { box-sizing: border-box; margin: 0; padding: 0; }
  html, body {
    width: 1200px; height: 835px; overflow: hidden;
    background: var(--paper);
  }
  .sheet { position: relative; width: 1200px; height: 835px; }
  .card {
    position: absolute;
    width: 573px; height: 315px;
    background: var(--navy);
  }
  .card--framed { border: 7px solid var(--teal); }
  .card--a { left: 27px;  top: 102px; }
  .card--b { left: 613px; top: 102px; }
  .card--c { left: 27px;  top: 436px; }
  .card--d { left: 613px; top: 436px; }

  .brand {
    position: absolute;
    display: flex; align-items: center; justify-content: center;
    border: 1.5px solid var(--teal);
    border-radius: 50%;
    color: var(--teal);
    font-family: "Questrial", sans-serif;
    text-align: center;
    line-height: 1.1;
  }
  .brand--front { width: 180px; height: 180px; font-size: 30px; }
  .brand--back  { width: 140px; height: 140px; font-size: 23px; }

  .card--framed .brand--front { left: 196px; top: 61px; }
  .card--c .brand--front { left: 197px; top: 68px; }
  .card--framed .brand--back { left: 105px; top: 75px; }
  .card--d .brand--back { left: 122px; top: 84px; }

  .contact {
    position: absolute;
    color: var(--teal);
  }
  .card--b .contact { left: 349px; top: 80px; }
  .card--d .contact { left: 353px; top: 87px; }

  .contact__name {
    font-family: "Questrial", sans-serif;
    font-size: 17px;
    letter-spacing: 0.2px;
    line-height: 1;
  }
  .contact__role {
    font-family: "Questrial", sans-serif;
    font-size: 12px;
    letter-spacing: 28px;
    margin-top: 5px;
    line-height: 1;
  }
  .contact__list { list-style: none; margin-top: 24px; }
  .contact__item {
    display: flex; align-items: center;
    height: 20px;
    font-family: "Open Sans", sans-serif;
    font-weight: 300;
    font-size: 12px;
  }
  .contact__item--small { font-size: 11px; }
  .contact__item + .contact__item { margin-top: 0.5px; }
  .contact__icon {
    width: 14px; height: 14px;
    margin-right: 11px;
    fill: var(--teal);
    flex: none;
  }
  .social {
    display: flex; gap: 18px;
    margin-top: 6px;
    font-family: "Open Sans", sans-serif;
    font-weight: 300;
    font-size: 11px;
  }
  .social__handle { display: flex; align-items: center; }
  .social__dot {
    width: 10px; height: 10px;
    margin-right: 7px;
    border-radius: 50%;
    background: var(--teal);
    flex: none;
  }
  .tagline {
    position: absolute;
    left: 0; right: 0; bottom: 16px;
    text-align: center;
    color: var(--teal);
    font-family: "Questrial", sans-serif;
    font-size: 10px;
    letter-spacing: 3px;
    text-transform: uppercase;
  }
</style>
</head>
<body>
<main class="sheet">

  <section class="card card--framed card--a" aria-label="Card front, framed">
    <div class="brand brand--front">Lil' Tot<br>Nook</div>
  </section>

  <section class="card card--framed card--b" aria-label="Card back, framed">
    <div class="brand brand--back">Lil' Tot<br>Nook</div>
    <div class="contact">
      <p class="contact__name">WENDELL J.FERRIS</p>
      <p class="contact__role">owner</p>
      <ul class="contact__list">
        <li class="contact__item">
          <svg class="contact__icon" viewBox="0 0 16 16"><path d="M1 6l7-4 7 4v8H1z"/><path d="M1 6l7 5 7-5" fill="none" stroke="#1f2532" stroke-width="1.2"/></svg>
          sales@ltotnook.com
        </li>
        <li class="contact__item contact__item--small">
          <svg class="contact__icon" viewBox="0 0 16 16"><path d="M3 1.5l3 3-1.6 1.8c.9 2 2.4 3.5 4.3 4.3L10.5 9l3 3-1.7 2.2C6.5 13.6 2.4 9.5 1 4z"/></svg>
          787-203-6159
        </li>
        <li class="contact__item contact__item--small">
          <svg class="contact__icon" viewBox="0 0 16 16"><path d="M1 5c0-2 14-2 14 0v1.5h-3.5V5h-7v1.5H1z"/><path d="M4 7h8l2 7H2z"/><circle cx="8" cy="10.5" r="1.6" fill="#1f2532"/></svg>
          787-203-6742
        </li>
        <li class="contact__item">
          <svg class="contact__icon" viewBox="0 0 16 16"><circle cx="8" cy="8" r="7"/><g fill="none" stroke="#1f2532" stroke-width="1"><ellipse cx="8" cy="8" rx="3" ry="7"/><path d="M1 8h14M2.5 4.5h11M2.5 11.5h11"/></g></svg>
          www.LTotNook.com
        </li>
      </ul>
      <div class="social">
        <span class="social__handle"><span class="social__dot"></span>/ltotnook</span>
        <span class="social__handle"><span class="social__dot"></span>@ltotnook</span>
      </div>
    </div>
    <p class="tagline">Handmade Baby Creations</p>
  </section>

  <section class="card card--c" aria-label="Card front">
    <div class="brand brand--front">Lil' Tot<br>Nook</div>
  </section>

  <section class="card card--d" aria-label="Card back">
    <div class="brand brand--back">Lil' Tot<br>Nook</div>
    <div class="contact">
      <p class="contact__name">WENDELL J.FERRIS</p>
      <p class="contact__role">owner</p>
      <ul class="contact__list">
        <li class="contact__item">
          <svg class="contact__icon" viewBox="0 0 16 16"><path d="M1 6l7-4 7 4v8H1z"/><path d="M1 6l7 5 7-5" fill="none" stroke="#1f2532" stroke-width="1.2"/></svg>
          sales@ltotnook.com
        </li>
        <li class="contact__item contact__item--small">
          <svg class="contact__icon" viewBox="0 0 16 16"><path d="M3 1.5l3 3-1.6 1.8c.9 2 2.4 3.5 4.3 4.3L10.5 9l3 3-1.7 2.2C6.5 13.6 2.4 9.5 1 4z"/></svg>
          787-203-6159
        </li>
        <li class="contact__item contact__item--small">
          <svg class="contact__icon" viewBox="0 0 16 16"><path d="M1 5c0-2 14-2 14 0v1.5h-3.5V5h-7v1.5H1z"/><path d="M4 7h8l2 7H2z"/><circle cx="8" cy="10.5" r="1.6" fill="#1f2532"/></svg>
          787-203-6742
        </li>
        <li class="contact__item">
          <svg class="contact__icon" viewBox="0 0 16 16"><circle cx="8" cy="8" r="7"/><g fill="none" stroke="#1f2532" stroke-width="1"><ellipse cx="8" cy="8" rx="3" ry="7"/><path d="M1 8h14M2.5 4.5h11M2.5 11.5h11"/></g></svg>
          www.LTotNook.com
        </li>
      </ul>
      <div class="social">
        <span class="social__handle"><span class="social__dot"></span>/ltotnook</span>
        <span class="social__handle"><span class="social__dot"></span>@ltotnook</span>
      </div>
    </div>
    <p class="tagline">Handmade Baby Creations</p>
  </section>

</main>
</body>
</html>
```